Personal Website for DBA of my main company

I need a website created for my personal brand for one of my Vinara of my main company. This website will be about my personal passion of wine. I am a certified sommelier and want a page that shows my passions for the wine industry. It will consist of pages that have video, pictures and possibly links to my cellar. (I have uploaded a screen shot of the only page I could find from a sommelier, I do not want to copy or look anything like this page....its just an idea of what one would look like)

Target Market(s)

Small, mostly word of mouth customers

Industry/Entity Type

Wine and Service Industry

Coding

Coded - Design and coding required

Number of Pages Required

4 page

Font styles to use
Other font styles liked:
• Font that is current but will be relevant in the future as well

Colors
0054AA
0677BA
7BADD7
CADEEF
E8F1F8
0094D4
00A9DD
6FCCEA
C7EBF8
E9F6FB
00AB8E
00BBA5
67D7C9
C6EFE9
E9F9F6
EB3D1F
EC4F4E
F09395
F8D3D4
FCEDEE

Requirements
Must have
• Landing page, video page and images page.

```html
<!DOCTYPE html>
<html lang="en">
<head>
<meta charset="utf-8">
<title>Vinara — Passion of Wine</title>
<link href="https://fonts.googleapis.com/css2?family=Marcellus&family=Lora:ital,wght@0,400;0,500;1,600&display=swap" rel="stylesheet">
<style>
:root{
  --navy:#0054AA;
  --blue:#0677BA;
  --sky:#0094D4;
  --cyan:#00A9DD;
  --aqua:#6FCCEA;
  --mist:#CADEEF;
  --ice:#E8F1F8;
  --teal:#00AB8E;
  --teal-2:#00BBA5;
  --red:#EB3D1F;
  --rose:#EC4F4E;
  --dark:#0f2a44;
  --ink:#1c2733;
  --muted:#4f5b66;
  --light:#ffffff;
}
*{margin:0;padding:0;box-sizing:border-box}
html,body{width:1200px;height:4008px;overflow:hidden}
body{position:relative;background:var(--light);font-family:'Lora',serif;color:var(--ink)}
.abs{position:absolute}
.heading{font-family:'Marcellus',serif;font-weight:400}
.center{text-align:center}

/* top bar + nav */
.topbar{left:0;top:0;width:1200px;height:39px;background:var(--navy);color:#fff;font-size:13px}
.social{left:171px;top:12px;display:flex;gap:12px}
.social span{width:14px;height:14px;border-radius:50%;background:var(--mist);display:block}
.contact-top{right:175px;top:11px}
.nav{left:0;top:39px;width:1200px;height:81px;background:#fff;border-bottom:1px solid var(--ice)}
.logo{left:171px;top:20px;font-family:'Marcellus',serif;font-size:36px;color:var(--navy)}
.menu{right:175px;top:28px;display:flex;gap:36px;font-size:15px}
.menu a{color:var(--ink);text-decoration:none}
.menu a.active{color:var(--sky)}

/* hero */
.hero{left:0;top:120px;width:1200px;height:520px;background:linear-gradient(100deg,#6b4a35 0%,#8a6248 30%,#5a3f31 60%,#2f2521 100%)}
.hero-title{left:789px;top:110px;font-size:64px;line-height:64px;color:#fff;letter-spacing:2px}
.hero-text{left:789px;top:255px;width:250px;font-size:12px;line-height:21px;color:#fff}
.btn{color:#fff;font-size:14px;letter-spacing:2px;display:flex;align-items:center;justify-content:center}
.btn-red{background:var(--red)}
.btn-teal{background:var(--teal)}
.hero-btn{left:792px;top:333px;width:154px;height:43px}
.hero-arrow{top:200px}
.diamond{left:563px;top:602px;width:74px;height:74px;background:var(--sky);transform:rotate(45deg)}

/* about */
.about-deco{left:0;top:790px;width:120px;height:410px;background:radial-gradient(ellipse at left,var(--ice),rgba(255,255,255,0) 70%)}
.about-title{left:186px;top:812px;width:400px;font-size:58px;color:var(--navy)}
.about-lead{left:156px;top:918px;width:460px;font-size:15px;font-style:italic;font-weight:600}
.about-text{left:176px;top:958px;width:420px;font-size:16px;line-height:22px;color:var(--muted)}
.signature{left:286px;top:1070px;width:200px;height:60px;background:linear-gradient(90deg,var(--ice),#f5f9fc);border-radius:4px}
.sig-name{left:236px;top:1138px;width:300px;font-size:14px;color:var(--muted)}
.about-photo{left:641px;top:708px;width:384px;height:513px;background:linear-gradient(150deg,#6b4b36,#8a6a58 40%,#c0392b 70%,#3a3030)}

/* services */
.services{left:0;top:1302px;width:1200px;height:599px;background:var(--blue);color:#fff}
.sec-title{font-size:58px;width:1200px;left:0}
.service{width:260px;text-align:center}
.service .art{width:140px;height:170px;margin:0 auto;background:rgba(255,255,255,.16);border-radius:8px}
.service h3{font-family:'Marcellus',serif;font-weight:400;font-size:24px;margin-top:20px}
.service p{font-size:16px;line-height:22px;margin-top:6px;color:var(--ice)}
.service a{display:inline-block;margin-top:20px;font-size:14px;letter-spacing:1.5px;color:#fff;text-decoration:none;border-bottom:1px solid var(--aqua);padding-bottom:2px}
.btn-outline{left:512px;top:503px;width:176px;height:42px;border:1.5px solid #fff;color:#fff;font-size:14px;letter-spacing:2px;display:flex;align-items:center;justify-content:center}

/* processing */
.proc-title{color:var(--navy)}
.proc-deco{left:1045px;top:1960px;width:155px;height:375px;background:linear-gradient(90deg,rgba(232,241,248,0),var(--ice))}
.step{width:166px;text-align:center;top:2159px}
.step .ico{width:100px;height:100px;margin:0 auto;border:1.5px dashed var(--cyan);border-radius:50%;display:flex;align-items:center;justify-content:center;color:var(--teal)}
.step h4{font-weight:400;font-size:18px;margin-top:24px;color:var(--navy)}
.step p{font-size:13px;line-height:19px;color:var(--muted);margin-top:10px;padding:0 14px}

/* collection */
.collection{left:0;top:2578px;width:1200px;height:517px;background:var(--navy);color:#fff}
.coll-deco{left:1040px;top:0;width:160px;height:420px;background:radial-gradient(ellipse at right,rgba(111,204,234,.25),rgba(255,255,255,0) 70%)}
.bottle-card{top:139px;width:203px;height:309px;border:1px solid rgba(202,222,239,.6);text-align:center}
.bottle{width:60px;height:206px;margin:9px auto 0;border-radius:22px 22px 6px 6px}
.bottle-card h4{font-family:'Marcellus',serif;font-weight:400;font-size:19px;margin-top:6px}
.bottle-card p{font-size:12px;line-height:18px;margin-top:6px;padding:0 12px;color:var(--mist)}
.sq-arrow{top:263px;width:39px;height:39px;background:var(--red);display:flex;align-items:center;justify-content:center}

/* blog */
.blog-title{left:162px;top:3160px;font-size:58px;color:var(--navy)}
.blog-intro{left:461px;top:3164px;width:400px;font-size:13px;line-height:19px;color:var(--muted)}
.blog-btn{left:875px;top:3162px;width:150px;height:45px}
.post{top:3249px;width:274px}
.post .img{height:179px}
.post .meta{font-size:11px;color:var(--sky);margin-top:15px}
.post h4{font-weight:400;font-size:17px;margin-top:4px;color:var(--ink)}
.post p{font-size:12.5px;line-height:19px;color:var(--muted);margin-top:10px}
.post a{display:inline-block;margin-top:10px;font-size:14px;letter-spacing:1.5px;color:var(--red);text-decoration:none;border-bottom:1px solid var(--red)}

/* footer */
.footer{left:0;top:3633px;width:1200px;height:375px;background:var(--dark);color:var(--mist);font-size:13px}
.f-logo{left:171px;top:68px;font-family:'Marcellus',serif;font-size:30px;color:#fff}
.f-info{left:171px;top:124px;display:flex;flex-direction:column;gap:18px;width:190px;line-height:20px}
.f-info div{display:flex;gap:8px;align-items:flex-start}
.f-info svg{flex:none;margin-top:3px}
.divider{top:58px;width:1px;height:238px;background:#2a4763}
.divider::after{content:"";position:absolute;left:-2px;top:90px;width:4px;height:20px;background:var(--teal-2)}
.f-head{font-family:'Marcellus',serif;font-size:20px;color:var(--aqua)}
.f-list{display:flex;flex-direction:column;gap:19px;margin-top:18px}
.f-input{left:817px;top:115px;width:210px;height:33px;background:#fff;color:var(--muted);font-size:13px;padding:8px 9px}
.f-sub{left:817px;top:157px;width:210px;height:33px;font-size:13px}
.f-rule{left:171px;top:319px;width:856px;height:1px;background:#2a4763}
.copy{left:0;top:333px;width:1200px;font-size:11px;color:var(--mist)}
.copy b{color:#fff;font-weight:400}
</style>
</head>
<body>

<div class="abs topbar">
  <div class="abs social"><span></span><span></span><span></span></div>
  <div class="abs contact-top">Contact Us 01 234 567 890</div>
</div>

<header class="abs nav">
  <div class="abs logo">Vinara</div>
  <nav class="abs menu">
    <a class="active" href="#">Home</a><a href="#">About</a><a href="#">Services</a><a href="#">Blog</a><a href="#">Contact</a>
  </nav>
</header>

<section class="abs hero" role="img" aria-label="Photo of friends sharing glasses of wine together">
  <svg class="abs hero-arrow" style="left:4px" width="40" height="74" viewBox="0 0 40 74"><polyline points="36,2 4,37 36,72" fill="none" stroke="#fff" stroke-width="2"/></svg>
  <svg class="abs hero-arrow" style="right:4px" width="40" height="74" viewBox="0 0 40 74"><polyline points="4,2 36,37 4,72" fill="none" stroke="#fff" stroke-width="2"/></svg>
  <h1 class="abs heading hero-title">Passion<br>of Wine</h1>
  <p class="abs hero-text">Lorem ipsum dolor sit amet, consectetur adipiscing elit, sed do eiusmod temidiunt ut labore et</p>
  <div class="abs btn btn-red hero-btn">KNOW MORE</div>
</section>
<div class="abs diamond"></div>
<svg class="abs" style="left:582px;top:628px" width="36" height="20" viewBox="0 0 36 20"><polyline points="2,2 18,17 34,2" fill="none" stroke="#fff" stroke-width="1.5"/></svg>

<div class="abs about-deco" role="img" aria-label="Faint grape vine illustration"></div>
<h2 class="abs heading about-title center">About Me</h2>
<svg class="abs" style="left:362px;top:878px;color:#00AB8E" width="48" height="34" viewBox="0 0 48 34"><g fill="none" stroke="currentColor" stroke-width="1.3"><circle cx="14" cy="14" r="5"/><circle cx="24" cy="14" r="5"/><circle cx="34" cy="14" r="5"/><circle cx="19" cy="23" r="5"/><circle cx="29" cy="23" r="5"/><circle cx="24" cy="30" r="3.5"/><path d="M24 9 V2"/></g></svg>
<p class="abs about-lead center">Lorem ipsum dolor sit amet, consectetur adipiscing elit</p>
<p class="abs about-text center">Duis vel dui et eros pharetra bibendum ac a urna. Aliquam pretium nunc sodales mattis interdum. Nam aliquet facilisis eleifend. Etiam urna justo, bibendum ut justo vitae, tincidunt ultricies sapien.</p>
<div class="abs signature" role="img" aria-label="Handwritten signature"></div>
<p class="abs sig-name center">Elias Marrow</p>
<div class="abs about-photo" role="img" aria-label="Portrait of the sommelier holding a wine box"></div>

<section class="abs services">
  <h2 class="abs heading sec-title center" style="top:58px">Services</h2>
  <div class="abs service" style="left:152px;top:158px"><div class="art" role="img" aria-label="Sketch of a wine barrel"></div><h3>Royal Wine</h3><p>Duis vel dui et eros pharetra bibendum ac a urna</p><a href="#">READ MORE</a></div>
  <div class="abs service" style="left:469px;top:158px"><div class="art" role="img" aria-label="Sketch of a wine decanter"></div><h3>Essentials</h3><p>Duis vel dui et eros pharetra bibendum ac a urna</p><a href="#">READ MORE</a></div>
  <div class="abs service" style="left:786px;top:158px"><div class="art" role="img" aria-label="Sketch of a wine bottle"></div><h3>Wine Tastings</h3><p>Duis vel dui et eros pharetra bibendum ac a urna</p><a href="#">READ MORE</a></div>
  <div class="abs btn-outline">VIEW ALL SERVICES</div>
</section>

<h2 class="abs heading sec-title proc-title center" style="top:1930px">Wine Processing</h2>
<div class="abs proc-deco" role="img" aria-label="Faint wine barrel illustration"></div>
<svg class="abs" style="left:0;top:0" width="1200" height="2500" viewBox="0 0 1200 2500">
  <path d="M184 2300 V2178 Q184 2116 246 2116 H288 Q350 2116 350 2178 V2403 Q350 2465 412 2465 H455 Q517 2465 517 2403 V2117 Q517 2055 579 2055 H623 Q685 2055 685 2117 V2403 Q685 2465 747 2465 H789 Q851 2465 851 2403 V2178 Q851 2116 913 2116 H956 Q1018 2116 1018 2178 V2300" fill="none" stroke="#0054AA" stroke-width="1.6"/>
  <circle cx="184" cy="2300" r="8" fill="#fff" stroke="#0054AA" stroke-width="1.6"/>
  <circle cx="1018" cy="2300" r="8" fill="#fff" stroke="#0054AA" stroke-width="1.6"/>
</svg>
<div class="abs step" style="left:184px"><div class="ico"><svg width="44" height="44" viewBox="0 0 44 44"><g fill="none" stroke="currentColor" stroke-width="1.4"><circle cx="14" cy="16" r="5"/><circle cx="24" cy="16" r="5"/><circle cx="34" cy="16" r="5"/><circle cx="19" cy="25" r="5"/><circle cx="29" cy="25" r="5"/><circle cx="24" cy="34" r="5"/><path d="M24 11 V3"/></g></svg></div><h4>Ripe grapes</h4><p>Duis vel dui et eros pharetra bibendum ac a urna. Aliquam pretium nunc sodal interdum.</p></div>
<div class="abs step" style="left:350px"><div class="ico"><svg width="44" height="44" viewBox="0 0 44 44"><g fill="none" stroke="currentColor" stroke-width="1.4"><rect x="8" y="18" width="28" height="14"/><path d="M12 32 V40 M32 32 V40 M16 18 V10 H28 V18"/></g></svg></div><h4>Crushing</h4><p>Duis vel dui et eros pharetra bibendum ac a urna. Aliquam pretium nunc sodal interdum.</p></div>
<div class="abs step" style="left:517px"><div class="ico"><svg width="44" height="44" viewBox="0 0 44 44"><g fill="none" stroke="currentColor" stroke-width="1.4"><path d="M6 22 H38"/><path d="M12 14 q-3 4 0 6 q3 -2 0 -6z M22 12 q-3 4 0 6 q3 -2 0 -6z M32 14 q-3 4 0 6 q3 -2 0 -6z"/><circle cx="14" cy="30" r="3"/><circle cx="30" cy="30" r="3"/></g></svg></div><h4>Filtration</h4><p>Duis vel dui et eros pharetra bibendum ac a urna. Aliquam pretium nunc sodal interdum.</p></div>
<div class="abs step" style="left:685px"><div class="ico"><svg width="44" height="44" viewBox="0 0 44 44"><g fill="none" stroke="currentColor" stroke-width="1.4"><rect x="8" y="20" width="28" height="20"/><path d="M16 20 V8 H20 V20 M26 20 V10 H30 V20"/><circle cx="22" cy="30" r="4"/></g></svg></div><h4>Bottling</h4><p>Duis vel dui et eros pharetra bibendum ac a urna. Aliquam pretium nunc sodal interdum.</p></div>
<div class="abs step" style="left:851px"><div class="ico"><svg width="44" height="44" viewBox="0 0 44 44"><g fill="none" stroke="currentColor" stroke-width="1.4"><path d="M6 20 L22 6 L38 20 V38 H6z"/><rect x="18" y="26" width="8" height="12"/><rect x="11" y="24" width="5" height="5"/><rect x="28" y="24" width="5" height="5"/></g></svg></div><h4>Degustation</h4><p>Duis vel dui et eros pharetra bibendum ac a urna. Aliquam pretium nunc sodal interdum.</p></div>

<section class="abs collection">
  <div class="abs coll-deco" role="img" aria-label="Faint grape vine illustration"></div>
  <h2 class="abs heading sec-title center" style="top:45px">Latest Collection</h2>
  <div class="abs sq-arrow" style="left:148px"><svg width="18" height="14" viewBox="0 0 18 14"><path d="M17 7 H2 M7 1 L1 7 L7 13" fill="none" stroke="#fff" stroke-width="1.6"/></svg></div>
  <div class="abs sq-arrow" style="left:1008px"><svg width="18" height="14" viewBox="0 0 18 14"><path d="M1 7 H16 M11 1 L17 7 L11 13" fill="none" stroke="#fff" stroke-width="1.6"/></svg></div>
  <div class="abs bottle-card" style="left:166px"><div class="bottle" role="img" aria-label="Bottle of red wine" style="background:linear-gradient(90deg,#111,#3a3a3a 40%,#111)"></div><h4>Chardonnay wine</h4><p>Lorem ipsum dolor sit amet, consectetur adipiscing elit.</p></div>
  <div class="abs bottle-card" style="left:386px"><div class="bottle" role="img" aria-label="Dark wine bottle" style="background:linear-gradient(90deg,#0d0d0d,#333 40%,#0d0d0d)"></div><h4>Chardonnay wine</h4><p>Lorem ipsum dolor sit amet, consectetur adipiscing elit.</p></div>
  <div class="abs bottle-card" style="left:604px"><div class="bottle" role="img" aria-label="Bottle of white wine" style="background:linear-gradient(90deg,#d9cf9a,#f5efd2 40%,#cdbd7a)"></div><h4>Chardonnay wine</h4><p>Lorem ipsum dolor sit amet, consectetur adipiscing elit.</p></div>
  <div class="abs bottle-card" style="left:823px"><div class="bottle" role="img" aria-label="Bottle of rosé wine" style="background:linear-gradient(90deg,#b8334a,#e8788a 40%,#b8334a)"></div><h4>Chardonnay wine</h4><p>Lorem ipsum dolor sit amet, consectetur adipiscing elit.</p></div>
</section>

<h2 class="abs heading blog-title">Latest Blog</h2>
<p class="abs blog-intro">Lorem ipsum dolor sit amet, consectetur adipiscing elit. Aenean interdum tincidunt interdum. Duis sollicitudin mauris lorem, eget fringilla odio scelerisque nec.</p>
<div class="abs btn btn-teal blog-btn">VIEW ALL</div>
<article class="abs post" style="left:171px"><div class="img" role="img" aria-label="Photo of the sommelier at a tasting" style="background:linear-gradient(120deg,#7a5a40,#4a5a7a 50%,#a89a80)"></div><p class="meta">Aug 18, 2022 &nbsp; Posted by Lorem</p><h4>Integer fermentum nisl ligula</h4><p>Sed commodo id velit id faucibus. In a mauris placerat, dictum tortor non, elementum nunc.</p><a href="#">READ MORE</a></article>
<article class="abs post" style="left:462px"><div class="img" role="img" aria-label="Photo of the sommelier presenting a bottle at a dinner table" style="background:linear-gradient(120deg,#8a3a2a,#3a4a8a 45%,#c8c0b4)"></div><p class="meta">Aug 18, 2022 &nbsp; Posted by Lorem</p><h4>Integer fermentum nisl ligula</h4><p>Sed commodo id velit id faucibus. In a mauris placerat, dictum tortor non, elementum nunc.</p><a href="#">READ MORE</a></article>
<article class="abs post" style="left:753px"><div class="img" role="img" aria-label="Illustrated portrait of the sommelier" style="background:linear-gradient(120deg,#8fd0ee,#6a5040 55%,#1a1a1a)"></div><p class="meta">Aug 18, 2022 &nbsp; Posted by Lorem</p><h4>Integer fermentum nisl ligula</h4><p>Sed commodo id velit id faucibus. In a mauris placerat, dictum tortor non, elementum nunc.</p><a href="#">READ MORE</a></article>

<footer class="abs footer">
  <div class="abs f-logo">Vinara</div>
  <div class="abs f-info">
    <div><svg width="14" height="14" viewBox="0 0 14 14"><path d="M7 1a4 4 0 0 0-4 4c0 3 4 8 4 8s4-5 4-8a4 4 0 0 0-4-4z" fill="#00BBA5"/></svg><span>Austria, Graz Weinweg 42</span></div>
    <div><svg width="14" height="14" viewBox="0 0 14 14"><path d="M3 1 L5 1 L6 4 L4.5 5.5 Q6 8.5 8.5 9.5 L10 8 L13 9 L13 11 Q13 13 11 13 Q1 12 1 3 Q1 1 3 1z" fill="#00BBA5"/></svg><span>01 234 567 890</span></div>
    <div><svg width="14" height="14" viewBox="0 0 14 14"><rect x="1" y="3" width="12" height="8" fill="#00BBA5"/><path d="M1 3 L7 8 L13 3" fill="none" stroke="#0f2a44" stroke-width="1"/></svg><span>info@vinara.com</span></div>
  </div>
  <div class="abs divider" style="left:367px"></div>
  <div class="abs divider" style="left:577px"></div>
  <div class="abs divider" style="left:773px"></div>
  <div class="abs" style="left:433px;top:66px"><div class="f-head">Quick Links</div><div class="f-list"><span>Home</span><span>About</span><span>Services</span><span>Blog</span><span>Contact</span></div></div>
  <div class="abs" style="left:635px;top:66px"><div class="f-head">Services</div><div class="f-list"><span>Royal Wine</span><span>Essentials</span><span>Wine Tastings</span><span>Others</span></div></div>
  <div class="abs f-head" style="left:815px;top:66px">Newsletter</div>
  <div class="abs f-input">Enter email address</div>
  <div class="abs btn btn-red f-sub">SUBSCRIBE</div>
  <div class="abs f-rule"></div>
  <p class="abs copy center">© 2022 <b>Vinara</b>. All right reserved</p>
</footer>

</body>
</html>
```